Bright Swipe Panel – Project specifications

Introduction:

Bright Swipe Panel (BSP) is an android screen unlock app allowing users to unlock their screen by opening one of their most used apps and so save the need to go to phone home screen and search for that app in order to open it.

Upon installation of the app end user will be presented with a screen that includes an End User License Agreement which the user will be able to Accept or Decline. Upon Acceptance user will be presented with a screen that includes a textual description of the app and an option to choose between a grid view and a list view and also to enable or disable the app. Once the user clicks Enable the app will close and the BSP functionality will start operating for the user. If the user hits Disable there will be another screen presented asking to user to confirm app disabling.

BSP Functionalities:

BSP Interface:
• The interface of BSP will be presented to users every time they wish to "wake-up" their device from lock scree state (typically by clicking home button or one of the side buttons of the device).
• BSP will allow user to unlock screen by selecting one of the apps installed on his/her device. Such selection will unlock the screen and open the selected app at the same time.
• BSP user interface will be presented as one of the followings:

(1) List View - a wall of stripes, each stripe will display an icon of a frequent or recent used app (following logic described below) and swiping such stripe from left to right or from right to left will unlock the screen and at the same time open the selected app so that user will be able to use the selected app immediately upon unlocking the screen.

or

(2) Grid View - a grid of apps following the same logic where each of the app icons can be tapped and dragged to open that app

List view screen:

• The BSP will present the Top 10 used apps in a form of stripes that are framed in the unlock screen. Each stripe will include an icon of the app in the middle of the stripe.
• User will be able to scroll up and down through the unlock screen without unlocking it
• User will be able to unlock screen by swiping the icon from left to right or from right to left and the design should hint that option. Doing this will unlock the screen and will open the app
• Two additional stripes - Stripe number four and the stripe before the last one will present an icon of an advertisement and these stripe will look slightl differently from other stripes.
The very last stripe will be a "Powered By Bright Swipe" stripe and swiping this stripe will open the Bright Swipe app. It should also look a little different from the others
• In case user has an unread text message or a missed call there will be an icon to indicate that and each of the icons will be presented as the first and second stripe from the top
• In addition - the very first stripe will have an unlock icon and it will also look a little different from app stripes as to indicate that swiping that stripe will just unlock the screen without opening a specific app
• At the bottom of the screen there will be a disabled button which will be activated by sliding that button upwards (and the design should indicate that). Once slides upwards it will open a screen with the text: "Are you sure you want to disable Bright Swipe Panel?" and it will have two buttons for yes and no.

SEE SAMPLE PLACEHOLDERS SCREENS FOR LIST VIEW ATTACHED TO PROJECT OVERVIEW

Grid View Screen:

• The BSP grid view screen will show a grid of 9 icons each (three icons in a raw) The middle icon in this grid will be an ad icon and it will look slightly different
• Below the grid there will be a stripe with unlock icon in the middle to indicate that swiping this stripe will unlock the screen without opening a specific app
• Below the strip there will be two rectangular banners - one can be swiped to the left and the other can be swiped to the right and they will be reserved for an ad icons and Powerd By icon that row will look a little different

SEE SAMPLE PLACEHOLDERS SCREENS FOR GRID VIEW ATTACHED TO PROJECT OVERVIEW

Graphic material needed:

• App icon indicating this is a Bright Swipe Panel App
• User agreement screen
• App description screen with ability to choose between list view and grid view + disable and enable
• List view screen (scrollable up and down - so this is a long screen)
• Grid view screen
• Disable confirmation screen

Attached sample screenshots. Hope this is clear....

```html
<!DOCTYPE html>
<html lang="en">
<head>
<meta charset="utf-8">
<title>Bright Swipe Panel – List View Themes</title>
<link rel="stylesheet" href="https://fonts.googleapis.com/css2?family=Open+Sans:wght@400;600&display=swap">
<style>
  :root {
    --page-bg: #f6f6f6;
    --white: #ffffff;
    --text-soft: rgba(255, 255, 255, 0.92);
    --line: rgba(255, 255, 255, 0.13);

    --red-header: #3b1215;
    --red-stripe-a: #b9252a;
    --red-stripe-b: #c3363a;
    --red-ad-row: #c43d40;
    --red-ad-box: #d26a6c;
    --red-ad-border: #8e1b1f;
    --red-bar: #2b0b0d;
    --red-tab: #4b2326;

    --green-header: rgba(22, 36, 24, 0.88);
    --green-bg: linear-gradient(160deg, #4d6a50 0%, #86a686 38%, #a3bda2 52%, #6f8f72 72%, #4a684d 100%);
    --green-bar: rgba(18, 28, 19, 0.9);
    --green-tab: rgba(55, 70, 56, 0.95);

    --dusk-header: rgba(16, 16, 26, 0.9);
    --dusk-bg: linear-gradient(180deg, #7c6f93 0%, #9b8a9b 20%, #6d6677 40%, #46504b 56%, #58704c 70%, #8a9a96 79%, #52673f 86%, #3d5230 100%);
    --dusk-bar: rgba(12, 14, 12, 0.88);
    --dusk-tab: rgba(50, 52, 50, 0.95);

    --status-bg: #000000;
    --status-accent: #33b5e5;
  }

  * { box-sizing: border-box; margin: 0; padding: 0; }

  html, body {
    width: 1200px;
    height: 830px;
    overflow: hidden;
    background: var(--page-bg);
    font-family: "Open Sans", Arial, sans-serif;
  }

  .canvas { position: relative; width: 1200px; height: 830px; }

  .sprite { position: absolute; width: 0; height: 0; overflow: hidden; }

  .screen {
    position: absolute;
    top: 133px;
    width: 334px;
    height: 569px;
    display: flex;
    flex-direction: column;
    overflow: hidden;
    color: var(--white);
  }
  .screen--green { left: 60px; background: var(--green-bg); }
  .screen--red   { left: 443px; background: var(--red-stripe-a); }
  .screen--dusk  { left: 830px; background: var(--dusk-bg); }

  .status-bar {
    position: absolute;
    left: 443px;
    top: 112px;
    width: 334px;
    height: 21px;
    background: var(--status-bg);
    display: flex;
    align-items: center;
    justify-content: flex-end;
    gap: 4px;
    padding-right: 8px;
    color: var(--status-accent);
    font-size: 11px;
  }
  .status-bar svg { width: 14px; height: 14px; fill: var(--status-accent); }
  .status-time { margin-left: 4px; }

  .stripe {
    position: relative;
    height: 55px;
    flex: 0 0 55px;
    display: flex;
    align-items: center;
    justify-content: center;
    border-top: 1px solid var(--line);
  }
  .stripe--unlock { border-top: none; }

  .screen--red .stripe:nth-child(odd)  { background: var(--red-stripe-a); }
  .screen--red .stripe:nth-child(even) { background: var(--red-stripe-b); }
  .screen--red .stripe--unlock { background: var(--red-header); }
  .screen--red .stripe--ad { background: var(--red-ad-row); }

  .screen--green .stripe:nth-child(odd)  { background: rgba(255, 255, 255, 0.05); }
  .screen--green .stripe:nth-child(even) { background: rgba(255, 255, 255, 0.11); }
  .screen--green .stripe--unlock { background: var(--green-header); }

  .screen--dusk .stripe:nth-child(odd)  { background: rgba(0, 0, 0, 0.06); }
  .screen--dusk .stripe:nth-child(even) { background: rgba(255, 255, 255, 0.07); }
  .screen--dusk .stripe--unlock { background: var(--dusk-header); }

  .chevrons {
    position: absolute;
    top: 50%;
    width: 62px;
    height: 26px;
    margin-top: -13px;
  }
  .chevrons--left  { left: 14px; }
  .chevrons--right { right: 14px; }

  .app-icon { width: 30px; height: 30px; }

  .app-name {
    font-size: 13px;
    font-weight: 600;
    color: var(--white);
    letter-spacing: 0.3px;
  }

  .ad-box {
    position: absolute;
    left: 7px;
    right: 7px;
    top: 9px;
    height: 38px;
    display: flex;
    align-items: center;
    justify-content: center;
    font-size: 10.5px;
    letter-spacing: 0.2px;
    text-transform: uppercase;
    color: var(--text-soft);
    border: 1px solid rgba(40, 60, 40, 0.55);
    background: rgba(255, 255, 255, 0.28);
  }
  .screen--red .ad-box { background: var(--red-ad-box); border-color: var(--red-ad-border); }
  .screen--dusk .ad-box { background: rgba(255, 255, 255, 0.24); border-color: rgba(20, 20, 30, 0.6); }

  .control-bar {
    position: relative;
    flex: 1 1 auto;
    display: flex;
    align-items: center;
    font-size: 10.5px;
    text-transform: uppercase;
    color: var(--text-soft);
  }
  .screen--green .control-bar { background: var(--green-bar); }
  .screen--red   .control-bar { background: var(--red-bar); }
  .screen--dusk  .control-bar { background: var(--dusk-bar); }

  .bar-arrow { position: absolute; top: 50%; width: 14px; height: 28px; margin-top: -14px; }
  .bar-arrow--left  { left: 10px; }
  .bar-arrow--right { right: 10px; }

  .powered-by {
    position: absolute;
    left: 26px;
    width: 102px;
    text-align: center;
    line-height: 13px;
  }

  .free-apps {
    position: absolute;
    left: 206px;
    width: 100px;
    text-align: center;
  }

  .disable-tab {
    position: absolute;
    left: 129px;
    top: 0;
    width: 78px;
    height: 100%;
    display: flex;
    flex-direction: column;
    align-items: center;
    justify-content: flex-end;
    padding-bottom: 12px;
  }
  .disable-tab::before {
    content: "";
    position: absolute;
    left: 50%;
    top: -14px;
    width: 48px;
    height: 48px;
    margin-left: -24px;
    border-radius: 50%;
    background: inherit;
  }
  .screen--green .disable-tab { background: var(--green-tab); }
  .screen--red   .disable-tab { background: var(--red-tab); }
  .screen--dusk  .disable-tab { background: var(--dusk-tab); }

  .disable-arrow { position: relative; width: 26px; height: 22px; margin-bottom: 9px; }
  .disable-label { position: relative; }
</style>
</head>
<body>
<div class="canvas">

  <svg class="sprite" aria-hidden="true">
    <defs>
      <symbol id="chev-left" viewBox="0 0 62 26">
        <g fill="none" stroke="#fff" stroke-linecap="square">
          <polyline points="13,2 3,13 13,24" stroke-width="2.6"/>
          <polyline points="25,2 15,13 25,24" stroke-width="1.6" opacity="0.65"/>
          <polyline points="37,2 27,13 37,24" stroke-width="1.4" opacity="0.38"/>
          <polyline points="49,2 39,13 49,24" stroke-width="1.2" opacity="0.18"/>
        </g>
      </symbol>
      <symbol id="chev-right" viewBox="0 0 62 26">
        <g fill="none" stroke="#fff" stroke-linecap="square">
          <polyline points="49,2 59,13 49,24" stroke-width="2.6"/>
          <polyline points="37,2 47,13 37,24" stroke-width="1.6" opacity="0.65"/>
          <polyline points="25,2 35,13 25,24" stroke-width="1.4" opacity="0.38"/>
          <polyline points="13,2 23,13 13,24" stroke-width="1.2" opacity="0.18"/>
        </g>
      </symbol>
      <symbol id="icon-unlock" viewBox="0 0 24 24">
        <g fill="none" stroke="#fff" stroke-width="1.3">
          <rect x="6" y="11" width="12" height="10" rx="0.5"/>
          <path d="M3 11V7a3.5 3.5 0 0 1 7 0v1"/>
          <circle cx="12" cy="15.2" r="1.1"/>
          <line x1="12" y1="16.3" x2="12" y2="18.2"/>
        </g>
      </symbol>
      <symbol id="icon-phone" viewBox="0 0 24 24">
        <path d="M7.5 3.5c-2.3 1.2-3.4 3.3-2.5 6.3 1.8 5.2 5.1 8.8 9.9 10.6 2.3.8 4.3-.1 5.3-2.1l-3.4-3-2.2 1.9c-2.8-1.2-4.8-3.6-5.8-6.2l2-2z" fill="none" stroke="#fff" stroke-width="1.3" stroke-linejoin="round"/>
      </symbol>
      <symbol id="icon-mail" viewBox="0 0 24 24">
        <g fill="none" stroke="#fff" stroke-width="1.3">
          <rect x="2.5" y="5.5" width="19" height="13"/>
          <polyline points="2.5,5.5 12,13 21.5,5.5"/>
          <polyline points="2.5,18.5 9.5,11.5"/>
          <polyline points="21.5,18.5 14.5,11.5"/>
        </g>
      </symbol>
      <symbol id="icon-music" viewBox="0 0 24 24">
        <g fill="#fff">
          <path d="M8 5.5 20 3v12.5h-1.6V6.2L9.6 8v10H8z"/>
          <ellipse cx="6" cy="18.2" rx="3" ry="2.3"/>
          <ellipse cx="16.4" cy="15.8" rx="3" ry="2.3"/>
        </g>
      </symbol>
      <symbol id="icon-calculator" viewBox="0 0 24 24">
        <g fill="#fff">
          <path d="M5.5 2h13v20h-13z M7 3.5v4.5h10V3.5z M7.5 10v2h2v-2z M11 10v2h2v-2z M14.5 10v2h2v-2z M7.5 13.5v2h2v-2z M11 13.5v2h2v-2z M14.5 13.5v2h2v-2z M7.5 17v2h2v-2z M11 17v2h2v-2z M14.5 17v2h2v-2z" fill-rule="evenodd"/>
        </g>
      </symbol>
      <symbol id="icon-contacts" viewBox="0 0 24 24">
        <g fill="none" stroke="#fff" stroke-width="1.3">
          <rect x="6" y="2.5" width="13.5" height="19" rx="1"/>
          <line x1="4" y1="6.5" x2="7.5" y2="6.5"/>
          <line x1="4" y1="12" x2="7.5" y2="12"/>
          <line x1="4" y1="17.5" x2="7.5" y2="17.5"/>
          <circle cx="12.8" cy="12" r="2"/>
          <path d="M14.8 12v1a1.3 1.3 0 0 0 2.4 0v-1a4.4 4.4 0 1 0-1.8 3.6"/>
        </g>
      </symbol>
      <symbol id="bar-left" viewBox="0 0 14 28">
        <polyline points="12,2 2,14 12,26" fill="none" stroke="#fff" stroke-width="2"/>
      </symbol>
      <symbol id="bar-right" viewBox="0 0 14 28">
        <polyline points="2,2 12,14 2,26" fill="none" stroke="#fff" stroke-width="2"/>
      </symbol>
      <symbol id="slide-up" viewBox="0 0 26 22">
        <g fill="none" stroke="#fff" stroke-width="1.8">
          <polyline points="2,11 13,2 24,11"/>
          <polyline points="2,20 13,11 24,20" opacity="0.7"/>
        </g>
      </symbol>
    </defs>
  </svg>

  <!-- Theme: green blur -->
  <section class="screen screen--green" role="img" aria-label="Soft green blurred backdrop behind the unlock stripes">
    <div class="stripe stripe--unlock">
      <svg class="chevrons chevrons--left"><use href="#chev-left"/></svg>
      <svg class="app-icon"><use href="#icon-unlock"/></svg>
      <svg class="chevrons chevrons--right"><use href="#chev-right"/></svg>
    </div>
    <div class="stripe">
      <svg class="chevrons chevrons--left"><use href="#chev-left"/></svg>
      <svg class="app-icon"><use href="#icon-phone"/></svg>
      <svg class="chevrons chevrons--right"><use href="#chev-right"/></svg>
    </div>
    <div class="stripe">
      <svg class="chevrons chevrons--left"><use href="#chev-left"/></svg>
      <svg class="app-icon"><use href="#icon-mail"/></svg>
      <svg class="chevrons chevrons--right"><use href="#chev-right"/></svg>
    </div>
    <div class="stripe stripe--ad"><div class="ad-box">Advertisement</div></div>
    <div class="stripe">
      <svg class="chevrons chevrons--left"><use href="#chev-left"/></svg>
      <span class="app-name">Chatter</span>
      <svg class="chevrons chevrons--right"><use href="#chev-right"/></svg>
    </div>
    <div class="stripe">
      <svg class="chevrons chevrons--left"><use href="#chev-left"/></svg>
      <svg class="app-icon"><use href="#icon-music"/></svg>
      <svg class="chevrons chevrons--right"><use href="#chev-right"/></svg>
    </div>
    <div class="stripe">
      <svg class="chevrons chevrons--left"><use href="#chev-left"/></svg>
      <svg class="app-icon"><use href="#icon-calculator"/></svg>
      <svg class="chevrons chevrons--right"><use href="#chev-right"/></svg>
    </div>
    <div class="stripe">
      <svg class="chevrons chevrons--left"><use href="#chev-left"/></svg>
      <span class="app-name">Reelo</span>
      <svg class="chevrons chevrons--right"><use href="#chev-right"/></svg>
    </div>
    <div class="stripe">
      <svg class="chevrons chevrons--left"><use href="#chev-left"/></svg>
      <svg class="app-icon"><use href="#icon-contacts"/></svg>
      <svg class="chevrons chevrons--right"><use href="#chev-right"/></svg>
    </div>
    <div class="control-bar">
      <svg class="bar-arrow bar-arrow--left"><use href="#bar-left"/></svg>
      <span class="powered-by">Powered by<br>Bright Swipe</span>
      <div class="disable-tab">
        <svg class="disable-arrow"><use href="#slide-up"/></svg>
        <span class="disable-label">Disable</span>
      </div>
      <span class="free-apps">Free apps</span>
      <svg class="bar-arrow bar-arrow--right"><use href="#bar-right"/></svg>
    </div>
  </section>

  <!-- Theme: red -->
  <div class="status-bar">
    <svg viewBox="0 0 14 14"><path d="M7 12 1 5.5a8.5 8.5 0 0 1 12 0z"/></svg>
    <svg viewBox="0 0 14 14"><path d="M2 13h2v-3H2zm3 0h2V8H5zm3 0h2V5H8zm3 0h2V2h-2z"/></svg>
    <svg viewBox="0 0 14 14"><path d="M5 1h4v1.5h1.5V13h-7V2.5H5z"/></svg>
    <span class="status-time">12:00</span>
  </div>
  <section class="screen screen--red">
    <div class="stripe stripe--unlock">
      <svg class="chevrons chevrons--left"><use href="#chev-left"/></svg>
      <svg class="app-icon"><use href="#icon-unlock"/></svg>
      <svg class="chevrons chevrons--right"><use href="#chev-right"/></svg>
    </div>
    <div class="stripe">
      <svg class="chevrons chevrons--left"><use href="#chev-left"/></svg>
      <svg class="app-icon"><use href="#icon-phone"/></svg>
      <svg class="chevrons chevrons--right"><use href="#chev-right"/></svg>
    </div>
    <div class="stripe">
      <svg class="chevrons chevrons--left"><use href="#chev-left"/></svg>
      <svg class="app-icon"><use href="#icon-mail"/></svg>
      <svg class="chevrons chevrons--right"><use href="#chev-right"/></svg>
    </div>
    <div class="stripe stripe--ad"><div class="ad-box">Advertisement</div></div>
    <div class="stripe">
      <svg class="chevrons chevrons--left"><use href="#chev-left"/></svg>
      <span class="app-name">Chatter</span>
      <svg class="chevrons chevrons--right"><use href="#chev-right"/></svg>
    </div>
    <div class="stripe">
      <svg class="chevrons chevrons--left"><use href="#chev-left"/></svg>
      <svg class="app-icon"><use href="#icon-music"/></svg>
      <svg class="chevrons chevrons--right"><use href="#chev-right"/></svg>
    </div>
    <div class="stripe">
      <svg class="chevrons chevrons--left"><use href="#chev-left"/></svg>
      <svg class="app-icon"><use href="#icon-calculator"/></svg>
      <svg class="chevrons chevrons--right"><use href="#chev-right"/></svg>
    </div>
    <div class="stripe">
      <svg class="chevrons chevrons--left"><use href="#chev-left"/></svg>
      <span class="app-name">Reelo</span>
      <svg class="chevrons chevrons--right"><use href="#chev-right"/></svg>
    </div>
    <div class="stripe">
      <svg class="chevrons chevrons--left"><use href="#chev-left"/></svg>
      <svg class="app-icon"><use href="#icon-contacts"/></svg>
      <svg class="chevrons chevrons--right"><use href="#chev-right"/></svg>
    </div>
    <div class="control-bar">
      <svg class="bar-arrow bar-arrow--left"><use href="#bar-left"/></svg>
      <span class="powered-by">Powered by<br>Bright Swipe</span>
      <div class="disable-tab">
        <svg class="disable-arrow"><use href="#slide-up"/></svg>
        <span class="disable-label">Disable</span>
      </div>
      <span class="free-apps">Free apps</span>
      <svg class="bar-arrow bar-arrow--right"><use href="#bar-right"/></svg>
    </div>
  </section>

  <!-- Theme: dusk landscape -->
  <section class="screen screen--dusk" role="img" aria-label="Landscape wallpaper of a mountain lake at dusk behind the unlock stripes">
    <div class="stripe stripe--unlock">
      <svg class="chevrons chevrons--left"><use href="#chev-left"/></svg>
      <svg class="app-icon"><use href="#icon-unlock"/></svg>
      <svg class="chevrons chevrons--right"><use href="#chev-right"/></svg>
    </div>
    <div class="stripe">
      <svg class="chevrons chevrons--left"><use href="#chev-left"/></svg>
      <svg class="app-icon"><use href="#icon-phone"/></svg>
      <svg class="chevrons chevrons--right"><use href="#chev-right"/></svg>
    </div>
    <div class="stripe">
      <svg class="chevrons chevrons--left"><use href="#chev-left"/></svg>
      <svg class="app-icon"><use href="#icon-mail"/></svg>
      <svg class="chevrons chevrons--right"><use href="#chev-right"/></svg>
    </div>
    <div class="stripe stripe--ad"><div class="ad-box">Advertisement</div></div>
    <div class="stripe">
      <svg class="chevrons chevrons--left"><use href="#chev-left"/></svg>
      <span class="app-name">Chatter</span>
      <svg class="chevrons chevrons--right"><use href="#chev-right"/></svg>
    </div>
    <div class="stripe">
      <svg class="chevrons chevrons--left"><use href="#chev-left"/></svg>
      <svg class="app-icon"><use href="#icon-music"/></svg>
      <svg class="chevrons chevrons--right"><use href="#chev-right"/></svg>
    </div>
    <div class="stripe">
      <svg class="chevrons chevrons--left"><use href="#chev-left"/></svg>
      <svg class="app-icon"><use href="#icon-calculator"/></svg>
      <svg class="chevrons chevrons--right"><use href="#chev-right"/></svg>
    </div>
    <div class="stripe">
      <svg class="chevrons chevrons--left"><use href="#chev-left"/></svg>
      <span class="app-name">Reelo</span>
      <svg class="chevrons chevrons--right"><use href="#chev-right"/></svg>
    </div>
    <div class="stripe">
      <svg class="chevrons chevrons--left"><use href="#chev-left"/></svg>
      <svg class="app-icon"><use href="#icon-contacts"/></svg>
      <svg class="chevrons chevrons--right"><use href="#chev-right"/></svg>
    </div>
    <div class="control-bar">
      <svg class="bar-arrow bar-arrow--left"><use href="#bar-left"/></svg>
      <span class="powered-by">Powered by<br>Bright Swipe</span>
      <div class="disable-tab">
        <svg class="disable-arrow"><use href="#slide-up"/></svg>
        <span class="disable-label">Disable</span>
      </div>
      <span class="free-apps">Free apps</span>
      <svg class="bar-arrow bar-arrow--right"><use href="#bar-right"/></svg>
    </div>
  </section>

</div>
</body>
</html>
```